New Business Card Design Project

Looking for a modern business card design for an import distribution business for industrial technical products. The winning design will translate modern, sophistication, technical, professional and sustainable.

Target Market(s)

Technical customers

Industry/Entity Type

Business

Contact Information for Business Card

Dean Harlow
Sales Manager
M: 0471 625 183
P: 1300 872 619
dean@volkarsystems.com.au
4/18 Galloway Crest Road
Marlow Heights NSW 2158
www.volkarsystems.com.au

Font styles to use
Sans Serif

Colors
ec1f27
606060
000000
fbfbfb

Requirements
Must have
• My Logo which is the Volkar Systems logo attached
Nice to have
• Eurostile Bold font

```html
<!DOCTYPE html>
<html lang="en">
<head>
<meta charset="utf-8">
<title>Volkar Systems – Business Card</title>
<link href="https://fonts.googleapis.com/css2?family=Orbitron:wght@700&family=Saira:wght@400;500&display=swap" rel="stylesheet">
<style>
  :root {
    --red: #ec1f27;
    --grey: #606060;
    --black: #000000;
    --paper: #fbfbfb;
    --stage: #2a2726;
    --back-card: #111111;
    --back-tile: #1c1c1c;
  }
  html, body {
    margin: 0;
    width: 1200px;
    height: 1200px;
    overflow: hidden;
    background: var(--stage);
  }
  .canvas { position: relative; width: 1200px; height: 1200px; }

  .card {
    position: absolute;
    width: 640px;
    height: 391px;
    box-shadow: 0 10px 30px rgba(0,0,0,.55);
    overflow: hidden;
  }

  /* back side */
  .card-back { left: 140px; top: 150px; background: var(--back-card); }
  .card-back .pattern {
    position: absolute; inset: 0;
    background: linear-gradient(135deg, var(--back-tile), #141414);
  }
  .card-back .brand {
    position: absolute; left: 0; right: 0; top: 166px;
    display: flex; justify-content: center; align-items: center; gap: 18px;
  }
  .brand-square { width: 54px; height: 54px; background: var(--red); }
  .brand-name {
    font-family: "Orbitron", sans-serif;
    font-weight: 700;
    color: var(--red);
    font-size: 36px;
    letter-spacing: 1px;
    text-transform: uppercase;
  }

  /* front side */
  .card-front { left: 420px; top: 650px; background: var(--paper); }
  .card-front .brand {
    position: absolute; right: 30px; top: 46px;
    display: flex; align-items: center; gap: 14px;
  }
  .card-front .brand-square { width: 44px; height: 44px; }
  .card-front .brand-name { font-size: 28px; }

  .rule { position: absolute; height: 1.5px; background: var(--red); }
  .rule-top { left: 0; top: 112px; width: 34px; }
  .rule-under { left: 148px; top: 150px; right: 0; }

  .person-name {
    position: absolute; left: 40px; top: 98px;
    font-family: "Orbitron", sans-serif;
    font-weight: 700;
    color: var(--red);
    font-size: 23px;
    letter-spacing: .5px;
    text-transform: uppercase;
    margin: 0;
    white-space: nowrap;
  }
  .person-title {
    position: absolute; left: 30px; top: 130px;
    font-family: "Saira", sans-serif;
    color: var(--grey);
    font-size: 13px;
    text-transform: uppercase;
    margin: 0;
  }

  .contacts {
    position: absolute; left: 30px; top: 176px;
    list-style: none; margin: 0; padding: 0;
    font-family: "Saira", sans-serif; color: var(--grey);
  }
  .contacts li { display: flex; align-items: center; gap: 12px; height: 25px; font-size: 15px; }
  .contacts li.email { font-size: 13.5px; }
  .icon { width: 15px; height: 15px; flex: none; }

  .address {
    position: absolute; left: 400px; top: 262px;
    font-family: "Saira", sans-serif; color: var(--grey);
    font-style: normal;
    font-size: 14.5px; line-height: 24px;
  }

  .footer-bands { position: absolute; left: 0; bottom: 0; width: 640px; height: 80px; }
  .website {
    position: absolute; right: 30px; bottom: 14px;
    font-family: "Saira", sans-serif; color: var(--red);
    font-size: 13.5px; letter-spacing: .3px;
  }
</style>
</head>
<body>
<main class="canvas">

  <section class="card card-back" aria-label="Business card back">
    <div class="pattern" role="img" aria-label="Grid of dark rounded squares pattern"></div>
    <div class="brand">
      <span class="brand-square"></span>
      <span class="brand-name">Volkar Systems</span>
    </div>
  </section>

  <section class="card card-front" aria-label="Business card front">
    <div class="brand">
      <span class="brand-square"></span>
      <span class="brand-name">Volkar Systems</span>
    </div>

    <span class="rule rule-top"></span>
    <span class="rule rule-under"></span>

    <p class="person-name">Dean Harlow</p>
    <p class="person-title">Sales Manager</p>

    <ul class="contacts">
      <li>
        <svg class="icon" viewBox="0 0 16 16" aria-hidden="true"><rect width="16" height="16" rx="2" fill="#ec1f27"/><rect x="5" y="3" width="6" height="10" rx="1" fill="none" stroke="#fbfbfb" stroke-width="1.4"/></svg>
        0471 625 183
      </li>
      <li>
        <svg class="icon" viewBox="0 0 16 16" aria-hidden="true"><rect width="16" height="16" rx="2" fill="#ec1f27"/><path d="M4.5 4c1-.8 1.8.6 2.2 1.6.3.7-.7 1-.5 1.7.4 1.2 1.6 2.4 2.8 2.8.7.2 1-.8 1.7-.5 1 .4 2.4 1.2 1.6 2.2-1.4 1.7-4.4.4-6.3-1.5S2.8 5.4 4.5 4z" fill="#fbfbfb"/></svg>
        1300 872 619
      </li>
      <li class="email">
        <svg class="icon" viewBox="0 0 16 16" aria-hidden="true"><rect width="16" height="16" rx="2" fill="#ec1f27"/><rect x="3" y="4.5" width="10" height="7" fill="#fbfbfb"/><path d="M3 4.5l5 4 5-4" fill="none" stroke="#ec1f27" stroke-width="1.2"/></svg>
        dean@volkarsystems.com.au
      </li>
    </ul>

    <address class="address">
      4/18 Galloway Crest Road<br>
      Marlow Heights NSW 2158
    </address>

    <svg class="footer-bands" viewBox="0 0 640 80" aria-hidden="true">
      <polygon points="0,18 330,18 310,38 0,38" fill="#ec1f27"/>
      <polygon points="345,12 640,12 640,80 0,80 0,52 310,52" fill="#000000"/>
    </svg>
    <span class="website">www.volkarsystems.com.au</span>
  </section>

</main>
</body>
</html>
```